HTML newsletter template for construction company

Hello. I need a company newsletter template made. Our website is: www.halvernbuildco.com

Can you please spend some time on our website and design a similarly themed newsletter template for us? We use infusionsoft, so it'd be great if someone has experience with infusionsoft's newsletter requirements.

Target Market(s)

All sized subcontracting companies. We are a national company but are headquartered in Phoenix, Az.

Industry/Entity Type

Construction Company

Font styles to use
Sans Serif

Requirements
Must have
• html
Nice to have
• We need a few different "sections" for content. We're planning on having an interview, a construction project spotlight, some type of article, tips of some-sort and provide a few upcoming events that we are participating in.

```html
<!DOCTYPE html>
<html lang="en">
<head>
<meta charset="utf-8">
<title>Halvern BuildCo Newsletter</title>
<link rel="stylesheet" href="https://fonts.googleapis.com/css2?family=Ubuntu:wght@400;500&family=Open+Sans:wght@400&family=Roboto:wght@900&display=swap">
<style>
  :root {
    --page-bg: #dedede;
    --card-bg: #ffffff;
    --card-border: #cfcfcf;
    --heading: #1c1c1c;
    --body-text: #9a9a9a;
    --link: #3a7bc8;
    --divider: #dcdcdc;
    --footer-bg: #222528;
    --footer-text: #d6d6d6;
    --footer-muted: #7d7f82;
    --note-text: #555555;
    --hero-top: #e9b92a;
    --hero-bottom: #f3d98e;
  }
  * { margin: 0; padding: 0; box-sizing: border-box; }
  html, body { width: 918px; height: 1200px; overflow: hidden; }
  body {
    position: relative;
    background: var(--page-bg);
    font-family: "Open Sans", Verdana, sans-serif;
    color: var(--body-text);
  }
  a { color: var(--link); }
  .abs { position: absolute; }

  .browser-note {
    top: 17px; left: 0; width: 918px; text-align: center;
    font-size: 9px; color: var(--note-text);
  }

  .card {
    top: 42px; left: 219px; width: 502px; height: 1093px;
    background: var(--card-bg);
    border: 1px solid var(--card-border);
    border-radius: 6px;
    overflow: hidden;
  }

  .brand { display: flex; align-items: center; gap: 10px; }
  .brand-mark {
    width: 48px; height: 48px; border-radius: 50%;
    background: var(--heading);
  }
  .brand-name {
    font-family: "Ubuntu", sans-serif; font-weight: 400;
    font-size: 27px; color: var(--heading); letter-spacing: -0.5px;
  }
  .header-brand { top: 55px; left: 237px; }
  .forward-link {
    top: 73px; left: 601px; font-size: 10px; color: var(--link);
    text-decoration: none;
  }

  .hero {
    top: 117px; left: 219px; width: 502px; height: 260px;
    background: linear-gradient(160deg, var(--hero-top) 0%, #d9a92a 35%, var(--hero-bottom) 100%);
  }
  .hero-headline {
    top: 222px; left: 375px;
    font-family: "Roboto", Arial, sans-serif; font-weight: 900;
    font-size: 37px; line-height: 47px; color: #0d0d0d;
    letter-spacing: -0.5px;
    text-shadow: 0 0 6px rgba(255,255,255,0.8);
  }

  .section-title {
    font-family: "Ubuntu", sans-serif; font-weight: 400;
    font-size: 17px; color: var(--heading);
  }
  .section-copy { font-size: 10px; line-height: 14.6px; }
  .read-more { font-size: 10px; }

  .photo-round { border-radius: 50%; }
  .interview-photo {
    top: 419px; left: 250px; width: 105px; height: 105px;
    background: radial-gradient(circle at 50% 40%, #c98a5c, #8a4a2a 70%, #5b3324);
  }
  .interview-rule {
    top: 420px; left: 384px; width: 2px; height: 100px;
    background: linear-gradient(#fff, #d6d6d6, #fff);
  }
  .interview-body { top: 419px; left: 400px; width: 300px; }

  .divider { left: 234px; width: 471px; border-top: 1px dashed var(--divider); }
  .divider-one { top: 549px; }
  .divider-two { top: 801px; }

  .spotlight-body { top: 574px; left: 234px; width: 305px; }
  .spotlight-photo {
    top: 574px; left: 563px; width: 142px; height: 203px;
    background: linear-gradient(180deg, #8a7a5e 0%, #c9c2b4 45%, #7f8796 100%);
  }

  .feature { top: 826px; width: 140px; }
  .feature-image {
    width: 102px; height: 102px; margin-left: 17px;
    border-radius: 50%;
  }
  .feature-shadow {
    width: 120px; height: 6px; margin: 2px 0 0 8px;
    background: radial-gradient(ellipse, rgba(0,0,0,0.15), transparent 70%);
  }
  .feature-title { margin-top: 22px; }
  .feature-copy { margin-top: 10px; }
  .feature .read-more { display: block; margin-top: 15px; }
  .feature-tips { left: 234px; }
  .feature-events { left: 400px; }
  .feature-identity { left: 566px; }
  .tips-image { background: radial-gradient(circle at 50% 40%, #f2c230, #3a4f8a 65%); }
  .events-image { background: radial-gradient(circle at 50% 60%, #ffffff 40%, #e24040 41%, #d9d9d9 70%); }
  .identity-image { background: radial-gradient(circle at 45% 45%, #a3a6aa, #2d2d2d 60%, #f5d12a 61%, #ffffff 75%); }

  .footer {
    top: 1086px; left: 219px; width: 502px; height: 49px;
    background: var(--footer-bg);
    border-left: 2px solid #3aa14a;
    border-radius: 0 0 6px 6px;
  }
  .footer-brand { top: 1099px; left: 232px; gap: 5px; }
  .footer-brand .brand-mark { width: 20px; height: 20px; background: var(--footer-text); }
  .footer-brand .brand-name { font-size: 12px; color: var(--footer-text); letter-spacing: 0; }
  .follow {
    top: 1100px; left: 520px; display: flex; align-items: center; gap: 8px;
    font-size: 16px; color: var(--footer-muted);
  }
  .social-dot { width: 14px; height: 14px; border-radius: 3px; background: var(--footer-muted); }

  .page-footer {
    top: 1150px; left: 0; width: 918px; text-align: center;
    font-size: 9px; line-height: 16.5px; color: var(--note-text);
  }
</style>
</head>
<body>
  <p class="abs browser-note">Having trouble viewing this email? <a href="#">View it in your browser</a></p>

  <div class="abs card"></div>

  <div class="abs brand header-brand">
    <span class="brand-mark"></span>
    <span class="brand-name">Halvern BuildCo</span>
  </div>
  <a class="abs forward-link" href="#">› Forward to a Friend</a>

  <div class="abs hero" role="img" aria-label="Photo of yellow levels and rulers lying on building blueprints"></div>
  <h1 class="abs hero-headline">STOP PLANNING.<br>START BUILDING.</h1>

  <div class="abs photo-round interview-photo" role="img" aria-label="Portrait of a smiling builder in a white hard hat"></div>
  <div class="abs interview-rule"></div>
  <div class="abs interview-body">
    <h2 class="section-title">Interview with Marcus Hale</h2>
    <p class="section-copy">Lorem ipsum dolor sit amet, consectetuer adipiscing elit, sed diam nonummy nibh euismoLorem ipsum dolor sit amet, consectetuer adipiscing elit,reet dolore...</p>
    <p class="read-more" style="margin-top:14px"><a href="#">Read More</a></p>
  </div>

  <div class="abs divider divider-one"></div>

  <div class="abs spotlight-body">
    <h2 class="section-title">Construction spotlight</h2>
    <p class="section-copy">Lorem ipsum dolor sit amet, consectetuer adipiscing elit, sed diam nonummy nibh euismoLorem ipsum dolor sit amet, consectetuer adipiscing elit,reet dolore sed diam nonummy nibh euismoLorem ipsum dolor sit amet, consectetuer adipiscing elit, reet dolor sit amet, consectetuer adipiscing elit, sed diam nonummy nibh euismoLorem ipsum dolor sit amet...</p>
    <p class="read-more" style="margin-top:14px"><a href="#">Read More</a></p>
  </div>
  <div class="abs spotlight-photo" role="img" aria-label="Photo of a foreman showing a couple their house under construction"></div>

  <div class="abs divider divider-two"></div>

  <div class="abs feature feature-tips">
    <div class="feature-image tips-image" role="img" aria-label="Photo of two construction workers in yellow hard hats"></div>
    <div class="feature-shadow"></div>
    <h3 class="section-title feature-title">Tips</h3>
    <p class="section-copy feature-copy">Epsum factorial non deposit quid pro quo hic escorol.</p>
    <a class="read-more" href="#">Read More</a>
  </div>
  <div class="abs feature feature-events">
    <div class="feature-image events-image" role="img" aria-label="Calendar illustration showing July 17"></div>
    <div class="feature-shadow"></div>
    <h3 class="section-title feature-title">Events</h3>
    <p class="section-copy feature-copy">Epsum factorial non deposit quid pro quo hic escorol.</p>
    <a class="read-more" href="#">Read More</a>
  </div>
  <div class="abs feature feature-identity">
    <div class="feature-image identity-image" role="img" aria-label="Photo of a steel hammer with a black and yellow grip"></div>
    <div class="feature-shadow"></div>
    <h3 class="section-title feature-title">Identity</h3>
    <p class="section-copy feature-copy">Epsum factorial non deposit quid pro quo hic escorol.</p>
    <a class="read-more" href="#">Read More</a>
  </div>

  <div class="abs footer"></div>
  <div class="abs brand footer-brand">
    <span class="brand-mark"></span>
    <span class="brand-name">Halvern BuildCo</span>
  </div>
  <div class="abs follow">
    <span>Follow:</span>
    <span class="social-dot"></span>
    <span class="social-dot"></span>
    <span class="social-dot"></span>
    <span class="social-dot"></span>
    <span class="social-dot"></span>
  </div>

  <p class="abs page-footer">Halvern Yard Bld. 4, 2210 Foundry Lane, Mesa AZ 85201 www.halvernbuildco.com news@halvernbuildco.com<br>Copyright © 2013 Halvern BuildCo. <a href="#" style="color:var(--note-text)">Unsubscribe</a></p>
</body>
</html>
```